Research, Writing and Editing business needs a Business Card Design

I need a business card design for a new company based in Melbourne called The Bellwood Advisory Group. We provide research, writing and editing services. The company logo is attached, but I am open to your creative designs for business cards with the logo. As you will note, there are two potential logos. Feel free to use either of the logos.

The overall look I am hoping for is sleek, sophisticated, feminine and elegant.

Thanks in advance for your efforts.

Target Market(s)

Business professionals, academics and students

Industry/Entity Type

Business

Font styles to use
Serif
Script

Colors

Designer to choose colors to be used in the design.

Requirements
Must have
• The Bellwood Advisory Group
Dr Tessa Brennig

M: 0458 293 647
E: tessa@thebellwoodadvisorygroup.com.au
W: thebellwoodadvisorygroup.com.au
Nice to have
• Research | Writing | Editing

```html
<!DOCTYPE html>
<html lang="en">
<head>
<meta charset="utf-8">
<title>The Bellwood Advisory Group – Business Card</title>
<link rel="stylesheet" href="https://fonts.googleapis.com/css2?family=Cinzel:wght@400&family=Great+Vibes&family=Didact+Gothic&display=swap">
<style>
  :root {
    --backdrop: #d9d7d3;
    --paper-light: #f4efe4;
    --paper-mid: #e9e0cc;
    --paper-edge: #c9b894;
    --ink: #1c1b19;
    --ink-soft: #2a2926;
    --quill-tone: #3a3834;
  }
  html, body {
    margin: 0;
    padding: 0;
    width: 1200px;
    height: 720px;
    overflow: hidden;
    background: var(--backdrop);
  }
  .canvas {
    width: 1200px;
    height: 720px;
    display: flex;
    align-items: center;
    justify-content: center;
    gap: 40px;
  }
  .card {
    position: relative;
    width: 520px;
    height: 300px;
    box-sizing: border-box;
    overflow: hidden;
    background:
      radial-gradient(ellipse at 50% 50%, var(--paper-light) 0%, var(--paper-light) 45%, var(--paper-mid) 78%, var(--paper-edge) 100%);
    box-shadow: 0 2px 6px rgba(0,0,0,0.18);
    color: var(--ink);
  }

  /* Back: personal details */
  .card-back .name-row {
    position: absolute;
    left: 56px;
    top: 44px;
    display: flex;
    align-items: center;
    gap: 18px;
  }
  .card-back .holder-name {
    margin: 0;
    font-family: "Great Vibes", cursive;
    font-weight: 400;
    font-size: 48px;
    line-height: 1.1;
    color: var(--ink);
    white-space: nowrap;
  }
  .card-back .quill-art {
    flex: none;
    width: 56px;
    height: 26px;
    margin-top: 14px;
  }
  .card-back .contact-list {
    position: absolute;
    left: 86px;
    top: 140px;
    margin: 0;
    padding: 0;
    list-style: none;
    font-family: "Didact Gothic", sans-serif;
    font-size: 17px;
    line-height: 34px;
    color: var(--ink-soft);
    white-space: nowrap;
  }
  .card-back .contact-list li:first-child { padding-left: 92px; }

  /* Front: company name */
  .card-front .brand {
    position: absolute;
    left: 40px;
    right: 40px;
    top: 112px;
    display: flex;
    align-items: center;
    justify-content: center;
    gap: 12px;
  }
  .card-front .brand-mark {
    flex: none;
    width: 18px;
    height: 18px;
    background: var(--ink);
  }
  .card-front .brand-name {
    margin: 0;
    font-family: "Cinzel", serif;
    font-weight: 400;
    font-size: 16px;
    letter-spacing: 0.12em;
    color: var(--ink);
    white-space: nowrap;
  }
</style>
</head>
<body>
  <main class="canvas">
    <section class="card card-back" aria-label="Business card back">
      <div class="name-row">
        <h1 class="holder-name">Dr Tessa Brennig</h1>
        <svg class="quill-art" role="img" aria-label="Quill feather illustration" viewBox="0 0 56 26">
          <rect x="0" y="0" width="56" height="26" rx="4" fill="var(--quill-tone)" opacity="0.7"/>
        </svg>
      </div>
      <ul class="contact-list">
        <li>M: 0458 293 647</li>
        <li>E: tessa@thebellwoodadvisorygroup.com.au</li>
        <li>W: thebellwoodadvisorygroup.com.au</li>
      </ul>
    </section>

    <section class="card card-front" aria-label="Business card front">
      <div class="brand">
        <span class="brand-mark" aria-hidden="true"></span>
        <p class="brand-name">The Bellwood Advisory Group</p>
      </div>
    </section>
  </main>
</body>
</html>
```